Fotograf sucht Gutschein-Design
Zielgruppe
Bin Fotograf spezialisiert auf Pärchen und Hochzeitsfotos
Aufgabenstellung
Möchte einen neuen Gutschein für meine Zwecke haben. Sollte zu meinem fotografischen Stil passen, hell/ freundlich/ Retro? Vintage? Kann auch gerne 'Verzierung' mit Blümchen/ Zweige enthalten wenns passt. am besten ein wenig auf meiner Homepage orientieren >>> www.jonaskeltermann.com - Auch meine Logo/ Firmendaten sollten wo passend platziert sein. Mein Logo/ und Fotos füge ich bei und können wie es gut passt verwendet werden. Das auf dem Einzelbild bin ich, falls es wo passt wäre es toll. Schriftmäßig sollte es natürlich irgendwie das Wort Gutschein enthalten. Dann noch 'von' und 'für' und ein Feld wo ich händisch die Gutscheinnummer eintragen kann. Das Format/ Form überlasse ich auch ganz euch aber werde voraussichtlich bei blattkurier bestellen. (Falls es um das finden des passenden Formats/ Form geht). Bei Fragen könnt ihr euch gerne jederzeit melden.

```html
<!DOCTYPE html>
<html lang="de">
<head>
<meta charset="utf-8">
<title>Gutschein – Jonas Keltermann Fotografie</title>
<link rel="stylesheet" href="https://fonts.googleapis.com/css2?family=Great+Vibes&family=Jost:wght@400&display=swap">
<style>
  :root {
    --paper: #ffffff;
    --panel: #efefef;
    --ink: #111111;
    --frame: #222222;
    --twig: #d8c7b0;
  }
  html, body {
    margin: 0;
    padding: 0;
    width: 1200px;
    height: 426px;
    overflow: hidden;
    background: var(--paper);
  }
  .voucher {
    position: relative;
    width: 1200px;
    height: 426px;
    background: var(--paper);
    font-family: "Jost", "Helvetica Neue", Arial, sans-serif;
    color: var(--ink);
  }
  .voucher__frame {
    position: absolute;
    left: 42px; top: 16px;
    width: 1156px; height: 409px;
    border: 1px solid var(--frame);
    box-sizing: border-box;
  }
  .voucher__panel {
    position: absolute;
    left: 59px; top: 34px;
    width: 555px; height: 374px;
    background: var(--panel);
  }
  .voucher__twig {
    position: absolute;
    left: 26px; top: 8px;
    width: 140px; height: 142px;
    border-radius: 50%;
    background: radial-gradient(ellipse at 55% 50%, rgba(216,199,176,0.6), rgba(216,199,176,0) 70%);
  }
  .voucher__title {
    position: absolute;
    left: 84px; top: 74px;
    margin: 0;
    font-family: "Great Vibes", "Brush Script MT", cursive;
    font-weight: 400;
    font-size: 128px;
    line-height: 1;
    letter-spacing: 3px;
    color: var(--ink);
  }
  .fields {
    position: absolute;
    left: 94px; top: 262px;
    margin: 0; padding: 0;
    list-style: none;
    font-size: 20px;
  }
  .fields__row {
    display: flex;
    align-items: flex-end;
    height: 28px;
  }
  .fields__label { width: 76px; }
  .fields__line {
    width: 152px;
    border-bottom: 1.5px solid var(--ink);
    margin-bottom: 5px;
  }
  .fields__row--number { margin-top: 18px; }
  .fields__row--number .fields__label { width: auto; margin-right: 4px; }
  .fields__row--number .fields__line { width: 152px; }
  .gallery__photo { position: absolute; }
  .photo--boat   { left: 629px;  top: 34px;  width: 181px; height: 121px; background: linear-gradient(135deg, #b9a796, #6e7f8c 60%, #d9d2c8); }
  .photo--grass  { left: 817px;  top: 34px;  width: 181px; height: 121px; background: linear-gradient(160deg, #6f8a4e, #3f5a2c 55%, #a8b88a); }
  .photo--cliff  { left: 1004px; top: 34px;  width: 178px; height: 121px; background: linear-gradient(180deg, #c9d4dc, #bfb9ae 50%, #d8cfc4); }
  .photo--stones { left: 629px;  top: 160px; width: 181px; height: 121px; background: linear-gradient(135deg, #a39a8e, #cfc7bc 55%, #8d8479); }
  .photo--forest { left: 817px;  top: 160px; width: 181px; height: 121px; background: linear-gradient(160deg, #c6d3d6, #6c7f3e 50%, #b88b3a); }
  .photo--tree   { left: 1004px; top: 160px; width: 178px; height: 248px; background: linear-gradient(170deg, #a9b7bd, #8e9a8a 40%, #7f6249 75%, #a66a3a); }
  .photo--beach  { left: 629px;  top: 286px; width: 181px; height: 122px; background: linear-gradient(160deg, #d7d2c9, #b6aa9a 50%, #4d5258); }
  .photo--walk   { left: 817px;  top: 286px; width: 181px; height: 122px; background: linear-gradient(180deg, #dfe5e8, #7d8f5a 45%, #e2dccf); }
  .brand {
    position: absolute;
    left: 428px; top: 316px;
    width: 186px;
    text-align: center;
    color: var(--ink);
    font-family: "Jost", "Helvetica Neue", Arial, sans-serif;
    font-weight: 400;
  }
  .brand__name {
    margin: 0;
    font-size: 21px;
    line-height: 26px;
    white-space: nowrap;
  }
  .brand__tag {
    margin: 6px 0 0;
    font-size: 18px;
    line-height: 22px;
  }
</style>
</head>
<body>
<main class="voucher">
  <div class="voucher__frame"></div>
  <div class="voucher__panel"></div>
  <div class="voucher__twig" role="img" aria-label="Zarter beiger Zweig als Verzierung"></div>

  <h1 class="voucher__title">Gutschein</h1>

  <ul class="fields">
    <li class="fields__row"><span class="fields__label">Betrag:</span><span class="fields__line"></span></li>
    <li class="fields__row"><span class="fields__label">von:</span><span class="fields__line"></span></li>
    <li class="fields__row"><span class="fields__label">für:</span><span class="fields__line"></span></li>
    <li class="fields__row fields__row--number"><span class="fields__label">Gutscheinnummer:</span><span class="fields__line"></span></li>
  </ul>

  <section class="gallery" aria-label="Paarfotos">
    <div class="gallery__photo photo--boat" role="img" aria-label="Foto: Paar umarmt sich in einem alten Boot"></div>
    <div class="gallery__photo photo--grass" role="img" aria-label="Foto: Paar steht in hohem grünem Gras"></div>
    <div class="gallery__photo photo--cliff" role="img" aria-label="Foto: Paar sitzt auf Felsen am Meer"></div>
    <div class="gallery__photo photo--stones" role="img" aria-label="Foto: Paar sitzt auf Kieselsteinen"></div>
    <div class="gallery__photo photo--forest" role="img" aria-label="Foto: Paar auf einem Waldweg im Herbst"></div>
    <div class="gallery__photo photo--tree" role="img" aria-label="Foto: Fotograf sitzt an einem Baum auf einem Felsen"></div>
    <div class="gallery__photo photo--beach" role="img" aria-label="Foto: Babybauch-Shooting am Strand"></div>
    <div class="gallery__photo photo--walk" role="img" aria-label="Foto: Paar spaziert Hand in Hand an der Küste"></div>
  </section>

  <div class="brand">
    <p class="brand__name">Jonas Keltermann</p>
    <p class="brand__tag">Fotografie</p>
  </div>
</main>
</body>
</html>
```